Label design for high quality nutritional supplement brand

We need a new label design for our dietary supplement brand "NorlumPlus" from Germany. We sell high-quality nutritional supplements that help improve overall well-being.

All products in our range should receive the new label. You can find our current design on our homepage norlumplus-shop.example. The new design should be completely redesigned and look modern, fresh, high quality, minimalist and clean. We prefer the colors nude, green and earth tones.

The newly created label should contain our NorlumPlus logo. For this reason you will find this file attached. You will also find our current label, which needs to be renewed, in the appendix.

Colors

Designer to choose colors to be used in the design.

Requirements
Must have
• NorlumPlus logo

```html
<!DOCTYPE html>
<html lang="de">
<head>
<meta charset="utf-8">
<title>NorlumPlus Complex – Etikett</title>
<link rel="stylesheet" href="https://fonts.googleapis.com/css2?family=Inter:wght@300;400;600;700&display=swap">
<style>
  :root {
    --backdrop-top: #c4c4c4;
    --backdrop-bottom: #ececec;
    --label-white: #ffffff;
    --ink: #2a2a2a;
    --green-light: #b9d9a4;
    --green-mid: #98c47c;
    --green-strip-top: #8bbd6e;
    --green-strip-bottom: #2f6a1c;
    --text-light: #f4f9f0;
  }
  * { margin: 0; padding: 0; box-sizing: border-box; }
  html, body {
    width: 1200px;
    height: 960px;
    overflow: hidden;
  }
  body {
    background: linear-gradient(180deg, var(--backdrop-top), var(--backdrop-bottom));
    font-family: "Inter", sans-serif;
    display: flex;
    align-items: center;
    justify-content: center;
  }
  .label {
    width: 640px;
    height: 820px;
    background: var(--label-white);
    display: flex;
    flex-direction: column;
    box-shadow: 0 10px 30px rgba(0,0,0,0.08);
  }
  .label__brand {
    height: 360px;
    display: flex;
    align-items: center;
    justify-content: center;
  }
  .brand-name {
    display: flex;
    align-items: center;
    gap: 14px;
    font-weight: 300;
    font-size: 58px;
    color: var(--ink);
    letter-spacing: 0.5px;
  }
  .brand-name__dot {
    width: 14px;
    height: 14px;
    border-radius: 50%;
    background: var(--ink);
  }
  .label__panel {
    flex: 1;
    display: flex;
    background: linear-gradient(135deg, var(--green-light), var(--green-mid));
  }
  .category-strip {
    width: 122px;
    background: linear-gradient(180deg, var(--green-strip-top), var(--green-strip-bottom) 95%);
    display: flex;
    align-items: flex-end;
    justify-content: center;
    padding-bottom: 56px;
  }
  .category-strip__text {
    writing-mode: vertical-rl;
    transform: rotate(180deg);
    color: var(--text-light);
    font-weight: 400;
    font-size: 22px;
    letter-spacing: 7px;
  }
  .panel__content {
    flex: 1;
    padding: 56px 40px 0 50px;
    color: var(--text-light);
  }
  .product-title {
    text-align: center;
    line-height: 1.05;
  }
  .product-title__line1 {
    font-size: 66px;
    font-weight: 400;
  }
  .product-title__line1 strong { font-weight: 700; }
  .product-title__line2 {
    display: block;
    font-size: 52px;
    font-weight: 400;
    margin-top: 6px;
  }
  .product-meta {
    margin-top: 96px;
    display: flex;
    justify-content: space-between;
    align-items: center;
  }
  .dot-row { display: flex; gap: 13px; }
  .dot-row span {
    width: 11px; height: 11px; border-radius: 50%;
    background: var(--text-light);
  }
  .contents {
    text-align: left;
    font-size: 16px;
    font-weight: 300;
    line-height: 1.35;
  }
  .contents strong { font-weight: 700; }
  .website {
    margin-top: 48px;
    text-align: center;
    font-size: 19px;
    font-weight: 400;
  }
</style>
</head>
<body>
  <main class="label">
    <section class="label__brand">
      <div class="brand-name"><span class="brand-name__dot"></span>NorlumPlus</div>
    </section>
    <section class="label__panel">
      <div class="category-strip">
        <span class="category-strip__text">MULTIVITAMIN</span>
      </div>
      <div class="panel__content">
        <h1 class="product-title">
          <span class="product-title__line1">Norlum<strong>Plus</strong></span>
          <span class="product-title__line2">Complex</span>
        </h1>
        <div class="product-meta">
          <div class="dot-row"><span></span><span></span><span></span><span></span><span></span></div>
          <div class="contents">Inhalt: 83.1g<br><strong>90</strong> Kapseln</div>
        </div>
        <p class="website">www.norlumplus-shop.example</p>
      </div>
    </section>
  </main>
</body>
</html>
```